Business card design needed

We need a business card design for our new company Velbrino Event Creations, based in Leeton NSW. We will however be serving the whole Riverina area. We plan any events like, Parties, Weddings ext. We would like to see designs that is vibrant but elegant. Mainly we would like to have our Name displayed on the front and all the other info at the back. We need a design that will catch the eye anywhere.Design FRONT AND BACK

Industry/Entity Type

Events

Contact Information for Business Card

Velbrino Event Creations
Tirsa Hallveck

0461539207
velbrino@quorvamail.com

Believe the Impossible

Requirements
Must have
• Elegant Coulors and Fonts

```html
<!DOCTYPE html>
<html lang="en">
<head>
<meta charset="utf-8">
<title>Velbrino Event Creations – Business Card</title>
<link href="https://fonts.googleapis.com/css2?family=Poiret+One&family=EB+Garamond&display=swap" rel="stylesheet">
<style>
  :root {
    --backdrop: #f2f2f2;
    --card-sage: #c9dccf;
    --ink: #4f5552;
    --flourish-dark: #8a918d;
    --flourish-faint: #dde8e1;
  }
  html, body {
    margin: 0;
    padding: 0;
    width: 1200px;
    height: 741px;
    overflow: hidden;
    background: var(--backdrop);
  }
  .canvas {
    position: relative;
    width: 1200px;
    height: 741px;
  }
  .card {
    position: absolute;
    left: 346px;
    width: 507px;
    height: 292px;
    background: var(--card-sage);
  }
  .card--front { top: 65px; }
  .card--back { top: 386px; }

  .flourish {
    position: absolute;
    border-radius: 9px;
  }
  .card--front .flourish {
    left: 198px;
    top: 92px;
    width: 108px;
    height: 18px;
    background: linear-gradient(90deg, transparent, var(--flourish-dark) 20%, var(--flourish-dark) 80%, transparent);
    opacity: 0.55;
  }
  .card--back .flourish {
    left: 36px;
    top: 120px;
    width: 186px;
    height: 28px;
    background: linear-gradient(90deg, transparent, var(--flourish-faint) 15%, var(--flourish-faint) 85%, transparent);
  }

  .company-name {
    position: absolute;
    left: 0;
    right: 0;
    top: 124px;
    margin: 0;
    text-align: center;
    font-family: "Poiret One", sans-serif;
    font-weight: 400;
    font-size: 24px;
    letter-spacing: 0.3px;
    color: var(--ink);
  }
  .person-name {
    position: absolute;
    left: 36px;
    top: 158px;
    margin: 0;
    font-family: "Poiret One", sans-serif;
    font-weight: 400;
    font-size: 24px;
    color: var(--ink);
  }
  .contact {
    position: absolute;
    left: 36px;
    top: 214px;
    margin: 0;
    font-family: "EB Garamond", serif;
    font-size: 14px;
    line-height: 19px;
    color: var(--ink);
  }
</style>
</head>
<body>
  <main class="canvas">
    <section class="card card--front">
      <div class="flourish" role="img" aria-label="Small decorative scroll flourish"></div>
      <h1 class="company-name">Velbrino Event Creations</h1>
    </section>

    <section class="card card--back">
      <div class="flourish" role="img" aria-label="Faint embossed scroll flourish"></div>
      <h2 class="person-name">Tirsa Hallveck</h2>
      <p class="contact">
        <span class="contact__phone">t: 0461539207</span><br>
        <span class="contact__email">velbrino@quorvamail.com</span>
      </p>
    </section>
  </main>
</body>
</html>
```